Business Card Design

We are a new residential construction company.our team is made up of young highly skilled tradesman of the next generation of carpenters coming through with new skills and ideas.we chose the name meridian as it means strikingly different from the rest as this is what we plan to be and we would like to portray this in our business card.we like Bold lettering as we want to make a statement, also the use of colour would be great as we want to stand out from the usual plain construction cards and logos.
I have attached a logo sketch I did as a rough idea if you can tidy it up or improve on it would be good.
I have also attached the LBP logo please include this on the card small but still legible.
open to any colourschemes ideas.
thanks
(note)please delete the LBP#804317 off from the card details please.
Industry/Entity Type
Construction
Contact Information for Business Card
MERIDIAN CONSTRUCTION LIMITED
Director:Tom Halvick
Mobile :0217364820
Email:Meridian.Construction@quillpost.example
Address:48 Wendle place,Ashgrove park 2091,Auckland
LBP#BP804317

```html
<!DOCTYPE html>
<html lang="en">
<head>
<meta charset="utf-8">
<title>Meridian Construction – Business Card</title>
<link rel="stylesheet" href="https://fonts.googleapis.com/css2?family=Ubuntu:wght@400;500;700&display=swap">
<style>
  :root {
    --navy: #221f5c;
    --cyan: #29a8d8;
    --cyan-light: #8fd6ec;
    --white: #ffffff;
    --backdrop: #e4e4e6;
    --ink: #221f5c;
  }
  * { box-sizing: border-box; margin: 0; padding: 0; }
  html, body { width: 1200px; height: 1200px; overflow: hidden; }
  body {
    background: var(--backdrop);
    font-family: "Ubuntu", sans-serif;
    display: flex;
    align-items: center;
    justify-content: center;
    gap: 30px;
  }
  .card {
    position: relative;
    width: 560px;
    height: 327px;
    box-shadow: 0 4px 14px rgba(0,0,0,0.18);
    overflow: hidden;
  }

  /* Front */
  .card-front { background: var(--white); }
  .side-band {
    position: absolute; left: 0; top: 0; bottom: 0;
    width: 104px; background: var(--navy);
  }
  .wordmark {
    position: absolute; left: 30px; top: 52px;
    font-weight: 700; color: var(--cyan);
    font-size: 30px; line-height: 1.05; letter-spacing: 1px;
    text-transform: uppercase;
  }
  .details { position: absolute; left: 104px; top: 180px; right: 24px; color: var(--ink); }
  .person-name { padding-left: 8px; font-size: 23px; font-weight: 400; }
  .person-role { padding-left: 8px; font-size: 13px; color: var(--cyan); }
  .rule { height: 1px; background: var(--cyan-light); margin: 1px 0 9px 0; width: 430px; }
  .company { padding-left: 8px; font-size: 13.5px; letter-spacing: .2px; }
  .address { padding-left: 8px; font-size: 13px; margin-top: 2px; }
  .contact-row { position: relative; font-size: 13.5px; margin-top: 5px; padding-left: 8px; }
  .contact-icon {
    position: absolute; left: -22px; top: 1px;
    width: 13px; height: 13px; border-radius: 3px; background: var(--cyan);
  }
  .contact-icon svg { display: block; width: 13px; height: 13px; }
  .lbp-badge {
    position: absolute; right: 20px; bottom: 14px;
    width: 82px; height: 82px; border-radius: 50%;
    background: var(--white); border: 3px solid #1a1a1a;
  }
  .lbp-badge::after {
    content: ""; position: absolute; inset: 16px; border-radius: 50%; background: #1a1a1a;
  }

  /* Back */
  .card-back { background: var(--navy); display: flex; align-items: center; justify-content: center; }
  .wordmark-back {
    color: var(--white); font-weight: 700; font-size: 38px;
    text-align: center; line-height: 1.05; letter-spacing: 1.5px; text-transform: uppercase;
  }
</style>
</head>
<body>
  <section class="card card-front">
    <div class="side-band"></div>
    <div class="wordmark">Meridian<br>Construction</div>
    <div class="details">
      <p class="person-name">Tom Halvick</p>
      <p class="person-role">Director</p>
      <div class="rule"></div>
      <p class="company">MERIDIAN CONSTRUCTION LIMITED</p>
      <p class="address">48 Wendle place,Ashgrove park 2091,Auckland</p>
      <p class="contact-row">
        <span class="contact-icon"><svg viewBox="0 0 13 13"><path d="M4 3l1.5 1.5-1 1.2a6 6 0 0 0 2.8 2.8l1.2-1L10 9l-1 1.3C6 10 3 7 2.7 4z" fill="#fff"/></svg></span>
        0217364820
      </p>
      <p class="contact-row">
        <span class="contact-icon"><svg viewBox="0 0 13 13"><rect x="2.5" y="3.5" width="8" height="6" fill="none" stroke="#fff" stroke-width="1"/><path d="M2.5 3.5l4 3.2 4-3.2" fill="none" stroke="#fff" stroke-width="1"/></svg></span>
        Meridian.Construction@quillpost.example
      </p>
    </div>
    <div class="lbp-badge" role="img" aria-label="Licensed building practitioner badge"></div>
  </section>

  <section class="card card-back">
    <div class="wordmark-back">Meridian<br>Construction</div>
  </section>
</body>
</html>
```